Herbal tea shop web designing - Leafwell

We need a business-charity purpose online shop selling premium herbal teas with a tagline "Healthy with a heart" where all the raw materials are being purchased from Indonesian local farmers in order to give them sustainable employment. Every 20% from the total amount of the customer's purchase from our website always goes back to their communities to help build better sanitation, education or whatever they need. We need page to blog too and another page for customers to interact and share their thought. we expect an eye catching simple earthy (maybe a bit rustic) design with some brush lettering font in some parts. Thank you.

Target Market(s)

-Tea Lovers
-Anyone with body weight issues or any health issues in general

Industry/Entity Type

Home Health Care

Number of Pages Required

5+ page

Font styles to use
Other font styles liked:
• brush lettering font in some parts

Requirements
Must have
• - Brush lettering font
• -Simple, a bit rustic design with some nice watercolor touch
• -Blogging Page
• -catchy yet fancy and elegant E-commerce page
Nice to have
• Well, I will let the designers use their skills and imaginations to the fullest.

```html
<!DOCTYPE html>
<html lang="en">
<head>
<meta charset="utf-8">
<title>Leafwell — Herbal Tea Shop</title>
<link rel="stylesheet" href="https://fonts.googleapis.com/css2?family=Great+Vibes&family=Raleway:wght@400;500;600;700&display=swap">
<style>
:root{
  --cream:#f7eedb;
  --gold:#e0a82e;
  --gold-deep:#a07a2c;
  --ink:#2b2a27;
  --text:#4a4844;
  --teal:#4cc79a;
  --dark:#1b1a18;
  --pager:#8c8579;
  --white:#ffffff;
  --blush:#f2c9d2;
  --header-icon:#9a7424;
}
*{box-sizing:border-box;margin:0;padding:0}
html,body{width:1041px;height:1200px;overflow:hidden;background:var(--cream);font-family:'Raleway',sans-serif;color:var(--text)}
.page{position:relative;width:1041px;height:1200px}
.abs{position:absolute}
.script{font-family:'Great Vibes',cursive}

/* header */
.site-header{left:0;top:0;width:1041px;height:208px;background:linear-gradient(180deg,#6d5426 0%,#7a6130 45%,#5e4520 100%)}
.social{display:flex;gap:7px}
.social span{width:26px;height:26px;border-radius:50%;display:block}
.social-header span{background:var(--header-icon)}
.social-header span.active{background:var(--gold)}
.social-footer span{background:var(--white)}
.nav{display:flex;font-size:8px;font-weight:600}
.nav a{text-decoration:none;margin-left:22px}
.nav-header a{color:var(--gold)}
.nav-footer a{color:var(--white)}
.search{left:650px;top:41px;width:260px;height:25px;border-radius:13px;background:rgba(255,255,255,.22);color:#fff;font-size:8px;font-weight:600;padding:9px 13px;letter-spacing:.2px}
.search svg{position:absolute;right:10px;top:5px}
.brand{left:0;width:1041px;top:100px;text-align:center;font-weight:600;font-size:38px;color:var(--gold);letter-spacing:3px}

.divider{left:280px;width:480px;height:2px;background:var(--gold);opacity:.8}

/* hero */
.photo{border-radius:6px;overflow:hidden}
.hero{left:131px;top:250px;width:495px;height:280px;background:radial-gradient(circle at 30% 60%,#a78a3a 0%,#6f8d3a 30%,#b7c9a0 60%,#e6e4d8 100%)}
.tile-top{left:639px;top:250px;width:273px;height:134px;background:linear-gradient(120deg,#4e7d1c,#8cbf2e 50%,#5a3a1c)}
.tile-bottom{left:639px;top:397px;width:273px;height:133px;background:linear-gradient(120deg,#2a2b2d,#4a4b4e 50%,#1d1d1f)}
.badge{position:absolute;background:#fdf9f7;border:2px solid var(--blush);border-radius:22px;text-align:center}
.badge .l1{font-size:24px;color:var(--ink);line-height:1}
.badge .l2{font-size:28px;color:var(--gold);line-height:1.2}
.badge.small .l1{font-size:15px}
.badge.small .l2{font-size:19px}
.btn-fill{display:inline-block;background:var(--teal);color:#fff;font-weight:700;font-size:9px;border-radius:5px}
.dots{left:144px;top:507px;display:flex;gap:4px}
.dots span{width:10px;height:10px;border-radius:50%;border:1.5px solid #fff}
.dots span.on{background:radial-gradient(circle,#fff 35%,transparent 40%)}

/* about */
.about{left:130px;top:543px;width:780px;height:210px;background:#fff;border-radius:5px;border-bottom:2px solid var(--gold);text-align:center}
.about h2{font-weight:400;font-size:32px;color:var(--ink);margin-top:12px;line-height:1.1}
.about h2 em{font-style:normal;color:var(--gold)}
.about h3{font-weight:400;font-size:27px;color:var(--ink);margin-top:2px;line-height:1.1}
.about p{font-size:9.5px;line-height:18.5px;width:520px;margin:6px auto 0;color:#3c3a36}
.btn-line{display:inline-block;border:2px solid var(--teal);color:var(--teal);border-radius:6px;font-weight:600;font-size:9px;text-transform:uppercase}
.about .btn-line{margin-top:9px;padding:7px 20px}

/* tabs */
.tabs{left:130px;top:766px;width:780px;height:27px;background:var(--dark);border-radius:4px;display:flex;overflow:hidden}
.tabs span{color:#fff;font-weight:700;font-size:9.5px;line-height:27px;padding:0 18px;text-transform:uppercase;white-space:nowrap}
.tabs span.active{background:var(--gold);padding:0 18px 0 18px;min-width:95px}

/* products */
.card{top:805px;width:185px;height:260px;background:#fff;border-radius:5px;text-align:center}
.card .pile{position:absolute;left:28px;top:55px;width:130px;height:70px;border-radius:50%;background:radial-gradient(ellipse at 50% 60%,#6f7a2a 0%,#8a8a34 45%,rgba(255,255,255,0) 72%)}
.card h4{position:absolute;top:180px;width:100%;font-weight:500;font-size:8.8px;line-height:11.5px;color:#4a4844}
.card .price{position:absolute;top:205px;width:100%;font-size:11px;color:#2b2a27}
.card .btn-line,.card .btn-fill{position:absolute;left:13px;top:221px;width:160px;height:27px;line-height:23px;font-size:9px}
.card .btn-fill{line-height:27px;font-weight:600}
.pager{top:1078px;width:33px;height:32px;background:var(--pager);border-radius:4px}
.pager svg{display:block;margin:8px auto}

/* footer */
.site-footer{left:0;top:1150px;width:1041px;height:50px;background:var(--gold-deep)}
.copyright{left:0;width:1041px;top:1182px;text-align:center;font-size:8px;color:#fff}
</style>
</head>
<body>
<div class="page">

  <header class="abs site-header" role="img" aria-label="Misty tea plantation hillside at dusk"></header>
  <div class="abs social social-header" style="left:130px;top:12px">
    <span aria-label="Social link 1"></span><span aria-label="Social link 2"></span><span class="active" aria-label="Social link 3"></span><span aria-label="Social link 4"></span>
  </div>
  <nav class="abs nav nav-header" style="right:131px;top:16px">
    <a href="#">My Account</a><a href="#">Need Help?</a><a href="#">Contact</a><a href="#">My Cart</a>
  </nav>
  <div class="abs search">SEARCH HERE
    <svg width="16" height="16" viewBox="0 0 16 16"><circle cx="7" cy="7" r="5.5" fill="none" stroke="#fff" stroke-width="1.3"/><line x1="11" y1="11" x2="15" y2="15" stroke="#fff" stroke-width="1.3"/></svg>
  </div>
  <div class="abs brand">Leafwell</div>

  <div class="abs divider" style="top:230px"></div>

  <section class="abs photo hero" role="img" aria-label="Glasses of herbal tea with fresh mint leaves">
    <svg class="abs" style="left:16px;top:115px" width="22" height="56" viewBox="0 0 22 56"><polyline points="20,2 2,28 20,54" fill="none" stroke="#fff" stroke-width="2"/></svg>
    <svg class="abs" style="left:457px;top:115px" width="22" height="56" viewBox="0 0 22 56"><polyline points="2,2 20,28 2,54" fill="none" stroke="#fff" stroke-width="2"/></svg>
    <div class="badge" style="left:249px;top:120px;width:190px;height:135px">
      <div class="l1 script" style="margin-top:20px">Lorem Ipsum</div>
      <div class="l2 script">Super Sale</div>
      <span class="btn-fill" style="margin-top:6px;padding:8px 20px">SHOP</span>
    </div>
  </section>
  <div class="abs dots"><span class="on"></span><span></span><span></span></div>

  <section class="abs photo tile-top" role="img" aria-label="Basket of fresh green tea leaves">
    <div class="badge small" style="left:103px;top:22px;width:150px;height:90px">
      <div class="l1 script" style="margin-top:18px">Lorem Ipsum</div>
      <div class="l2 script">Lorem Ipsum</div>
    </div>
  </section>
  <section class="abs photo tile-bottom" role="img" aria-label="Cast iron teapot on a dark table">
    <div class="badge small" style="left:103px;top:22px;width:150px;height:90px">
      <div class="l1 script" style="margin-top:18px">Lorem Ipsum</div>
      <div class="l2 script">Lorem Ipsum</div>
    </div>
  </section>

  <section class="abs about">
    <h2 class="script">Welcome to <em>Leafwell</em></h2>
    <h3 class="script">About Us</h3>
    <p>Lorem ipsum dolor sit amet, consectetur adipiscing elit. Donec mollis luctus mattis. Donec eu justo in tellus consectetur laoreet. Morbi porttitor dignissim ante, ut varius elit lacinia malesuada. Aliquam mollis est posuere magna egestas porta. Maecenas mauris neque, feugiat fermentum convallis eu, pellentesque non nunc.Lorem ipsum dolor sit amet, consectetur adipiscing elit. Donec mollis luctus mattis. fermentum convallis eu, pellentesque non nunc.</p>
    <span class="btn-line">More about us</span>
  </section>

  <nav class="abs tabs">
    <span class="active">What's new</span><span>Deal of the week</span><span>Super sellers</span><span>Categories</span>
  </nav>

  <article class="abs card" style="left:130px">
    <div class="pile" role="img" aria-label="Pile of dried herbal tea buds"></div>
    <h4>LOREM IPSUM DOLOR SIT AMET,<br>CONSTETUR ADIPING ELIT.</h4>
    <div class="price">4.50 $</div>
    <span class="btn-line">View details</span>
  </article>
  <article class="abs card" style="left:328px">
    <div class="pile" role="img" aria-label="Pile of dried chamomile flowers"></div>
    <h4>LOREM IPSUM DOLOR SIT AMET,<br>CONSTETUR ADIPING ELIT.</h4>
    <div class="price">9.99 $</div>
    <span class="btn-fill">VIEW DETAILS</span>
  </article>
  <article class="abs card" style="left:526px">
    <div class="pile" role="img" aria-label="Pile of loose green tea leaves"></div>
    <h4>LOREM IPSUM DOLOR SIT AMET,<br>CONSTETUR ADIPING ELIT.</h4>
    <div class="price">12.50 $</div>
    <span class="btn-line">View details</span>
  </article>
  <article class="abs card" style="left:725px">
    <div class="pile" role="img" aria-label="Pile of green cardamom pods"></div>
    <h4>LOREM IPSUM DOLOR SIT AMET,<br>CONSTETUR ADIPING ELIT.</h4>
    <div class="price">19.77 $</div>
    <span class="btn-line">View details</span>
  </article>

  <div class="abs pager" style="left:485px"><svg width="14" height="16" viewBox="0 0 14 16"><polyline points="11,1 3,8 11,15" fill="none" stroke="#fff" stroke-width="1.5"/></svg></div>
  <div class="abs pager" style="left:524px"><svg width="14" height="16" viewBox="0 0 14 16"><polyline points="3,1 11,8 3,15" fill="none" stroke="#fff" stroke-width="1.5"/></svg></div>

  <div class="abs divider" style="top:1130px"></div>

  <footer class="abs site-footer"></footer>
  <div class="abs social social-footer" style="left:130px;top:1163px">
    <span aria-label="Social link 1"></span><span aria-label="Social link 2"></span><span aria-label="Social link 3"></span><span aria-label="Social link 4"></span>
  </div>
  <nav class="abs nav nav-footer" style="right:131px;top:1172px">
    <a href="#">My Account</a><a href="#">Need Help?</a><a href="#">Contact</a><a href="#">My Cart</a>
  </nav>
  <div class="abs copyright">Copyright © 2017</div>

</div>
</body>
</html>
```